Business Card for innovative, tech/consultant company

We are specializing in bringing together Efficiency methodology and Technology for our Business customers. We would like an astonishing business Card that matches this idea.

Target Market(s)

Businesses of medium size or more

Industry/Entity Type

Business Consultant

Contact Information for Business Card

Name, Title, personal email, www, address, phone

Font styles to use
Sans Serif

Colors
3277b5

Requirements
Must have
• - innovative, efficient design
• - good readable
• - Colors must match our logo (blue and grey)
• - the attached font (is licensed by our Company) must be used (Syntax LT)
Should not have
• overloaded

```html
<!DOCTYPE html>
<html lang="en">
<head>
<meta charset="utf-8">
<title>Claravia – Business Card</title>
<link rel="stylesheet" href="https://fonts.googleapis.com/css2?family=Open+Sans:wght@400;600&display=swap">
<style>
  :root {
    --page: #e9e7e3;
    --card-black: #050505;
    --brand-blue: #1aa3dc;
    --band-grey: #b9bcc0;
    --logo-grey: #c9cacc;
    --text-white: #ffffff;
    --photo-light: #e4e6e8;
    --photo-mid: #b4b8bc;
    --photo-dark: #8a8f94;
  }
  * { box-sizing: border-box; margin: 0; padding: 0; }
  html, body {
    width: 1200px; height: 892px; overflow: hidden;
    background: var(--page);
    font-family: "Open Sans", Arial, sans-serif;
  }
  .card {
    position: absolute; left: 100px; top: 140px;
    width: 1000px; height: 612px;
    background: var(--card-black);
    border-radius: 6px; overflow: hidden;
    box-shadow: 0 10px 30px rgba(0,0,0,.25);
  }
  .card-art { position: absolute; inset: 0; }
  .card-info {
    position: absolute; right: 64px; top: 46px;
    text-align: right; color: var(--text-white);
  }
  .brand {
    display: flex; justify-content: flex-end; align-items: center; gap: 16px;
    margin-bottom: 26px;
  }
  .brand-mark { width: 22px; height: 22px; background: var(--brand-blue); }
  .brand-name {
    font-weight: 400; font-size: 104px; line-height: 1;
    color: var(--logo-grey); letter-spacing: -1px;
  }
  .person-name { font-weight: 600; font-size: 40px; line-height: 1.15; }
  .person-title { font-weight: 400; font-size: 30px; line-height: 1.2; margin-bottom: 22px; }
  .contact-list { list-style: none; }
  .contact-item {
    display: flex; justify-content: flex-end; align-items: center; gap: 14px;
    font-size: 28px; line-height: 1.3;
  }
  .contact-icon {
    width: 26px; height: 26px; background: var(--text-white);
    border-radius: 2px; flex: none;
  }
  .contact-icon svg { display: block; width: 26px; height: 26px; }
</style>
</head>
<body>
  <div class="card">
    <svg class="card-art" viewBox="0 0 1000 612" width="1000" height="612">
      <defs>
        <linearGradient id="photoTone" x1="0" y1="0" x2="1" y2="1">
          <stop offset="0" stop-color="var(--photo-light)"/>
          <stop offset="0.55" stop-color="var(--photo-mid)"/>
          <stop offset="1" stop-color="var(--photo-dark)"/>
        </linearGradient>
      </defs>
      <path class="band-blue" d="M0 0 H470 Q560 306 470 612 H0 Z" fill="var(--brand-blue)"/>
      <path class="band-grey" d="M0 0 H454 Q544 306 454 612 H0 Z" fill="var(--band-grey)"/>
      <path class="office-photo" role="img" aria-label="Photo of a bright modern office reception with plants"
            d="M0 0 H438 Q528 306 438 612 H0 Z" fill="url(#photoTone)"/>
    </svg>

    <div class="card-info">
      <div class="brand">
        <span class="brand-mark"></span>
        <span class="brand-name">Claravia</span>
      </div>
      <p class="person-name">Daniel Marsh</p>
      <p class="person-title">Director</p>
      <ul class="contact-list">
        <li class="contact-item">0412 555 019
          <span class="contact-icon"><svg viewBox="0 0 26 26"><path d="M8 5 l3 4 -2 2 q2 4 6 6 l2 -2 4 3 -2 3 q-8 0 -13 -10 z" fill="#000"/></svg></span>
        </li>
        <li class="contact-item">hello@claravia.com
          <span class="contact-icon"><svg viewBox="0 0 26 26"><rect x="5" y="8" width="16" height="11" fill="none" stroke="#000" stroke-width="2"/><path d="M5 8 l8 6 8 -6" fill="none" stroke="#000" stroke-width="2"/></svg></span>
        </li>
        <li class="contact-item">www.claravia.com
          <span class="contact-icon"><svg viewBox="0 0 26 26"><circle cx="13" cy="13" r="8" fill="none" stroke="#000" stroke-width="2"/><path d="M5 13 h16 M13 5 q-5 8 0 16 M13 5 q5 8 0 16" fill="none" stroke="#000" stroke-width="1.5"/></svg></span>
        </li>
        <li class="contact-item">PO Box 118 Moorfield 3910
          <span class="contact-icon"><svg viewBox="0 0 26 26"><path d="M4 13 l9 -8 9 8 h-3 v8 h-4 v-5 h-4 v5 h-4 v-8 z" fill="#000"/></svg></span>
        </li>
      </ul>
    </div>
  </div>
</body>
</html>
```